Flyer design for our aerial photography service

We need an 8.5x11 two sided design flyer that will showcase our aerial photography service. No pricing or text is needed aside from our logo and somewhere on the page the title "Aerial Photography". I would like it be a black background with our logo in white which I have attached. Please make it a creative stylish design that highlights the photos. Our Logo should be at the top. The logo should not be large and shouldnt be the focus of the page but should be fairly visible. I'm open to it being in different locations as well.

Industry/Entity Type

Real Estate

Font styles to use
Serif

Requirements
Must have
• Logo and photos and the title Aerial Photography
Nice to have
Should not have
• n/a

```html
<!DOCTYPE html>
<html lang="en">
<head>
<meta charset="utf-8">
<title>Aerial Photography Flyer</title>
<link href="https://fonts.googleapis.com/css2?family=Cinzel:wght@400&family=Crimson+Text:wght@400&display=swap" rel="stylesheet">
<style>
  :root {
    --backdrop: #c9c9c9;
    --page: #050505;
    --ink: #ffffff;
    --ink-muted: #d6d6d6;
    --photo-sky: #8fb4cf;
    --photo-green: #5f8a46;
    --photo-autumn: #b8792f;
    --photo-roof: #7d7a78;
    --photo-water: #4f8a86;
  }
  html, body {
    margin: 0;
    padding: 0;
    width: 1200px;
    height: 974px;
    overflow: hidden;
    background: var(--backdrop);
  }
  .canvas {
    position: relative;
    width: 1200px;
    height: 974px;
  }
  .page {
    position: absolute;
    top: 178px;
    width: 480px;
    height: 622px;
    background: var(--page);
    overflow: hidden;
    color: var(--ink);
  }
  .page--front { left: 78px; }
  .page--back  { left: 650px; }

  .brand {
    position: absolute;
    display: flex;
    flex-direction: column;
    align-items: center;
    font-family: "Cinzel", serif;
    font-weight: 400;
    color: var(--ink);
  }
  .brand__mark {
    width: 34px;
    height: 34px;
    border: 2px solid var(--ink);
    border-radius: 50%;
    box-sizing: border-box;
  }
  .brand__name {
    margin-top: 4px;
    font-size: 11px;
    letter-spacing: 0.4px;
    white-space: nowrap;
  }
  .page--front .brand { left: 44px; width: 60px; top: 14px; }

  .collage {
    position: absolute;
    left: 28px;
    top: 55px;
    width: 422px;
    height: 422px;
    border-radius: 50%;
    background:
      radial-gradient(circle at 50% 50%, rgba(95,138,70,0.9) 0 18%, transparent 40%),
      conic-gradient(from 20deg, var(--photo-sky), var(--photo-roof), var(--photo-green), var(--photo-water), var(--photo-autumn), var(--photo-green), var(--photo-roof), var(--photo-sky));
  }

  .title {
    position: absolute;
    left: 0;
    right: 0;
    margin: 0;
    font-family: "Cinzel", serif;
    font-weight: 400;
    text-transform: uppercase;
    text-align: center;
    white-space: nowrap;
    line-height: 1;
    color: var(--ink);
  }
  .page--front .title { top: 536px; font-size: 33px; }

  .backdrop-photo {
    position: absolute;
    inset: 0;
    background:
      radial-gradient(ellipse at 50% 55%, rgba(255,255,255,0.06), transparent 60%),
      linear-gradient(180deg, #141414 0%, #1c1c1c 40%, #202020 62%, #151515 80%, #0c0c0c 100%);
  }
  .lens {
    position: absolute;
    left: 171px;
    top: 134px;
    width: 160px;
    height: 160px;
    border-radius: 50%;
    background: radial-gradient(circle, #151515 0 56%, #4a4a4a 59%, #222 66%, #707070 72%, #1a1a1a 79%, transparent 81%);
    box-shadow: 0 0 50px 14px rgba(255,255,255,0.16);
  }
  .page--back .brand { left: 171px; width: 160px; top: 190px; }
  .page--back .brand__mark { width: 26px; height: 26px; }
  .page--back .brand__name { font-size: 9.5px; }
  .page--back .title { top: 418px; font-size: 30px; }

  .contact {
    position: absolute;
    left: 0;
    right: 0;
    top: 494px;
    margin: 0;
    font-family: "Crimson Text", serif;
    font-style: normal;
    text-align: center;
    color: var(--ink-muted);
    font-size: 11px;
    line-height: 17.6px;
  }
  .contact__company {
    font-size: 13.5px;
    color: var(--ink);
    letter-spacing: 0.2px;
    line-height: 20px;
  }
</style>
</head>
<body>
<main class="canvas">

  <section class="page page--front" aria-label="Flyer front">
    <div class="brand">
      <span class="brand__mark"></span>
      <span class="brand__name">Northgate</span>
    </div>

    <div class="collage" role="img" aria-label="Circular collage of aerial photographs of suburban homes, pools, lakeside docks and autumn trees"></div>

    <h1 class="title">Aerial Photography</h1>
  </section>

  <section class="page page--back" aria-label="Flyer back">
    <div class="backdrop-photo" role="img" aria-label="Darkened photograph of a large house framed by trees at dusk"></div>
    <div class="lens"></div>
    <div class="brand">
      <span class="brand__mark"></span>
      <span class="brand__name">Northgate</span>
    </div>
    <h2 class="title">Aerial Photography</h2>
    <address class="contact">
      <div class="contact__company">NORTHGATE PHOTOGRAPHY, LLC</div>
      <div>112 Harbor Row,</div>
      <div>Maple Falls, NJ 07400</div>
      <div>Telephone: +1 555 014 2290</div>
      <div>E-mail: hello@northgatephoto.com</div>
    </address>
  </section>

</main>
</body>
</html>
```